Open Door Dialogues: Classroom and Family Allies building brighter pupil futures.

This is a book that helps to prepare for and hold a standard conference that an educator would have with the parents of the students in the school. It is also about how to have problem-solving conferences around difficult issues using techniques from family therapy. Parent involvement is a key ingredient for student success, but most educators have no training in holding meetings with parents. This book fills that gap.

Target Market(s)

Teachers, principals, counselors, school psychologists, school nurses. Anyone who has conferences with the parents of their students.

Font styles to use
Sans Serif

Colors
85acd3
ffcf3e

Requirements
Must have
• I have several books coming up. I'd like something that could be carried over to the new ones without too many changes. They won't all be about education. I am a psychologist so most of my writings will cover subjects related to emotional intelligence.
Nice to have
• Something dignified that will pop out for those in the schools. I like the combination of a royal blue background with white and gold (not yellow) lettering.
Should not have
• I'd like it to be easy to read. Not too messy or too much stuff on the page.

```html
<!DOCTYPE html>
<html lang="en">
<head>
<meta charset="utf-8">
<title>Open Door Dialogues – Book Cover</title>
<link rel="stylesheet" href="https://fonts.googleapis.com/css2?family=Josefin+Sans:wght@300;600;700&family=Mulish:wght@400&display=swap">
<style>
  :root {
    --stage: #e9e9e7;
    --royal-deep: #161d63;
    --royal: #25317f;
    --royal-mid: #3b4f9c;
    --spot-blue: #85acd3;
    --gold: #ffcf3e;
    --gold-deep: #e3ad2c;
    --white: #ffffff;
    --wood-light: #b56d2c;
    --wood-dark: #6a3510;
  }
  * { margin: 0; padding: 0; box-sizing: border-box; }
  html, body {
    width: 1200px;
    height: 762px;
    overflow: hidden;
    background: var(--stage);
  }
  .canvas {
    position: relative;
    width: 1200px;
    height: 762px;
  }
  .book-cover {
    position: absolute;
    left: 366px;
    top: 31px;
    width: 467px;
    height: 700px;
    overflow: hidden;
    background:
      radial-gradient(ellipse 62% 42% at 50% 64%, var(--spot-blue) 0%, var(--royal-mid) 55%, rgba(37,49,127,0) 100%),
      linear-gradient(180deg, var(--royal-deep) 0%, var(--royal) 45%, var(--royal-mid) 100%);
    box-shadow: 0 10px 30px rgba(0,0,0,0.25);
  }
  .title {
    position: absolute;
    top: 52px;
    left: 0;
    width: 100%;
    text-align: center;
    font-family: "Josefin Sans", sans-serif;
    color: var(--gold);
    text-transform: uppercase;
    line-height: 1;
  }
  .title-line { display: block; }
  .title-bold {
    font-weight: 700;
    background: linear-gradient(180deg, var(--gold) 0%, var(--gold-deep) 100%);
    -webkit-background-clip: text;
    background-clip: text;
    color: transparent;
  }
  .title-line--first { font-size: 78px; letter-spacing: 2px; }
  .title-line--second { font-size: 92px; font-weight: 300; letter-spacing: 3px; margin-top: -2px; }
  .title-line--third { font-size: 58px; letter-spacing: 1px; margin-top: -4px; }
  .subtitle {
    position: absolute;
    top: 282px;
    left: 60px;
    width: 347px;
    text-align: center;
    font-family: "Mulish", sans-serif;
    font-weight: 400;
    font-size: 19px;
    line-height: 1.45;
    color: var(--white);
    letter-spacing: 0.3px;
  }
  .lectern-art {
    position: absolute;
    left: 88px;
    top: 395px;
    width: 291px;
    height: 305px;
    border-radius: 10px 10px 0 0;
    background: linear-gradient(180deg, rgba(181,109,44,0.85) 0%, rgba(106,53,16,0.9) 100%);
  }
</style>
</head>
<body>
  <main class="canvas">
    <section class="book-cover">
      <h1 class="title">
        <span class="title-line title-line--first title-bold">Open</span>
        <span class="title-line title-line--second">Door</span>
        <span class="title-line title-line--third title-bold">Dialogues</span>
      </h1>
      <p class="subtitle">Classroom and Family Allies building brighter pupil futures.</p>
      <div class="lectern-art" role="img" aria-label="Wooden lectern with a slim microphone under a soft blue spotlight"></div>
    </section>
  </main>
</body>
</html>
```